Coffeeshop menu for filter tip

We want to have a cannabis (coffeeshop) menu in the size 25mm wide x 60mm wide. Some examples attached.

it must have the following text:
Menu

WEED p/g
Velotrine €16
Cinderfox €14
Tide Rambler €14
Marigolden €16
Grand Pelican €14
Copper Comet €14

HASH p/g
Baltic Ember €12
Harbor Velvet€11
Plum Rova €14
Dusk Maple €10

Target Market(s)

tourist in Amsterdam

Requirements
Nice to have
• cannabis sign leaf
• No Cigarettes allowed symbol

```html
<!DOCTYPE html>
<html lang="en">
<head>
<meta charset="utf-8">
<title>Coffeeshop Menu</title>
<link rel="stylesheet" href="https://fonts.googleapis.com/css2?family=Oswald:wght@500;700&display=swap">
<style>
  :root {
    --paper: #ffffff;
    --ink: #000000;
    --leaf-green: #2e9a4a;
    --leaf-red: #e0262a;
    --skyline: #d9d9d9;
    --skyline-edge: #9a9a9a;
  }
  html, body {
    margin: 0;
    padding: 0;
    width: 1200px;
    height: 2884px;
    overflow: hidden;
    background: var(--paper);
  }
  .menu-card {
    position: relative;
    width: 1200px;
    height: 2884px;
    overflow: hidden;
    background: var(--paper);
    font-family: "Oswald", "Arial Narrow", sans-serif;
    color: var(--ink);
  }
  .leaf {
    position: absolute;
    border-radius: 50%;
    background: radial-gradient(circle at 45% 45%, var(--leaf-green) 0%, var(--leaf-green) 45%, var(--leaf-red) 62%, rgba(255,255,255,0) 72%);
    opacity: 0.9;
  }
  .title {
    position: absolute;
    left: 0;
    top: 0;
    width: 1200px;
    height: 600px;
    margin: 0;
  }
  .title text {
    font-family: "Oswald", "Arial Narrow", sans-serif;
    font-weight: 700;
    font-size: 630px;
  }
  .title .title-shadow { fill: var(--ink); }
  .title .title-face {
    fill: var(--paper);
    stroke: var(--ink);
    stroke-width: 8px;
    paint-order: stroke;
  }
  .price-list {
    position: absolute;
    left: 118px;
    width: 960px;
    margin: 0;
    padding: 0;
    list-style: none;
  }
  .price-list li {
    display: flex;
    justify-content: space-between;
    height: 111px;
    font-weight: 700;
    font-style: italic;
    font-size: 104px;
    line-height: 111px;
    letter-spacing: 4px;
    transform: skewX(-6deg);
  }
  .price-list .unit { padding-right: 10px; }
  .weed-list { top: 700px; }
  .hash-list { top: 1730px; }
  .skyline {
    position: absolute;
    left: 0;
    top: 2600px;
    width: 1200px;
    height: 284px;
    background: linear-gradient(to bottom, rgba(217,217,217,0) 0%, var(--skyline) 45%, var(--paper) 100%);
  }
  .city-name {
    position: absolute;
    left: 0;
    top: 2715px;
    width: 1200px;
    text-align: center;
    font-weight: 500;
    font-size: 170px;
    line-height: 1;
    letter-spacing: 6px;
    color: var(--paper);
    -webkit-text-stroke: 3px var(--skyline-edge);
  }
</style>
</head>
<body>
<main class="menu-card">
  <div class="leaf" role="img" aria-label="Cannabis leaf" style="left:-60px;top:-40px;width:520px;height:460px;"></div>
  <div class="leaf" role="img" aria-label="Cannabis leaf" style="left:640px;top:-30px;width:600px;height:480px;"></div>
  <div class="leaf" role="img" aria-label="Cannabis leaf" style="left:-40px;top:320px;width:420px;height:420px;"></div>
  <div class="leaf" role="img" aria-label="Cannabis leaf" style="left:840px;top:340px;width:400px;height:420px;"></div>
  <div class="leaf" role="img" aria-label="Cannabis leaf" style="left:420px;top:480px;width:360px;height:380px;"></div>

  <svg class="title" viewBox="0 0 1200 600" role="heading" aria-level="1" aria-label="MENU">
    <text class="title-shadow" x="72" y="542" textLength="1060" lengthAdjust="spacingAndGlyphs">MENU</text>
    <text class="title-face" x="58" y="530" textLength="1060" lengthAdjust="spacingAndGlyphs">MENU</text>
  </svg>

  <div class="leaf" role="img" aria-label="Cannabis leaf" style="left:-80px;top:1080px;width:420px;height:440px;"></div>
  <div class="leaf" role="img" aria-label="Cannabis leaf" style="left:660px;top:1360px;width:360px;height:360px;"></div>
  <div class="leaf" role="img" aria-label="Cannabis leaf" style="left:860px;top:1980px;width:380px;height:400px;"></div>
  <div class="leaf" role="img" aria-label="Cannabis leaf" style="left:-60px;top:2380px;width:420px;height:360px;"></div>
  <div class="leaf" role="img" aria-label="Cannabis leaf" style="left:820px;top:2380px;width:420px;height:380px;"></div>
  <div class="leaf" role="img" aria-label="Cannabis leaf" style="left:400px;top:2520px;width:420px;height:360px;"></div>

  <ul class="price-list weed-list">
    <li class="heading"><span>WEED</span><span class="unit">p/g</span></li>
    <li><span>Velotrine</span><span>€16</span></li>
    <li><span>Cinderfox</span><span>€14</span></li>
    <li><span>Tide Rambler</span><span>€14</span></li>
    <li><span>Marigolden</span><span>€16</span></li>
    <li><span>Grand Pelican</span><span>€14</span></li>
    <li><span>Copper Comet</span><span>€14</span></li>
  </ul>

  <ul class="price-list hash-list">
    <li class="heading"><span>HASH</span><span class="unit">p/g</span></li>
    <li><span>Baltic Ember</span><span>€12</span></li>
    <li><span>Harbor Velvet</span><span>€11</span></li>
    <li><span>Plum Rova</span><span>€14</span></li>
    <li><span>Dusk Maple</span><span>€10</span></li>
  </ul>

  <div class="skyline" role="img" aria-label="Amsterdam canal house skyline"></div>
  <div class="city-name">AMSTERDAM</div>
</main>
</body>
</html>
```